Commercial Construction Company

We need a business card design based on our current logo. We are a commercial general contractor based in Southern California that specializes in bank remodels. We would like to see designs that incorporate dark blue. The final design should portray an image of professionalism and quality.

If possible, I would like to add metallic foil to the design. Thank you

```html
<!DOCTYPE html>
<html lang="en">
<head>
<meta charset="utf-8">
<title>Harlow Commercial Builders – Business Card</title>
<link rel="stylesheet" href="https://fonts.googleapis.com/css2?family=Arimo:wght@400;700&display=swap">
<style>
  :root {
    --backdrop: #2e2826;
    --card: #141414;
    --card-edge: #1d1d1d;
    --ink: #ffffff;
    --ink-soft: #c9c9c9;
    --divider: #3a3a3a;
    --navy: #1f4f8f;
    --foil: #cfd2d6;
  }
  * { margin: 0; padding: 0; box-sizing: border-box; }
  html, body {
    width: 1200px; height: 844px; overflow: hidden;
    background: var(--backdrop);
    font-family: "Arimo", Arial, sans-serif;
  }
  .stage {
    position: relative; width: 1200px; height: 844px;
    display: flex; align-items: center; justify-content: center; gap: 40px;
  }
  .card {
    width: 540px; height: 309px;
    background: var(--card);
    border: 1px solid var(--card-edge);
    position: relative;
  }
  /* front */
  .card-front { display: flex; }
  .brand-zone {
    width: 265px; height: 100%;
    display: flex; align-items: center; justify-content: center; gap: 12px;
    border-right: 1px solid var(--divider);
  }
  .brand-dot {
    width: 30px; height: 30px; border-radius: 50%;
    background: var(--navy); flex: none;
  }
  .brand-name {
    color: var(--ink); font-weight: 700; font-size: 22px;
    line-height: 1.1; letter-spacing: 0.5px; text-transform: uppercase;
  }
  .contact-zone {
    padding: 62px 0 0 30px; color: var(--ink-soft); font-size: 14px;
  }
  .person-name { color: var(--ink); font-weight: 700; font-size: 17px; letter-spacing: 0.3px; }
  .person-role { margin-top: 1px; }
  .contact-list { list-style: none; margin-top: 10px; }
  .contact-list li { display: flex; align-items: center; gap: 7px; line-height: 19px; }
  .contact-list svg { width: 12px; height: 12px; fill: var(--ink-soft); flex: none; }
  .address { margin-top: 12px; line-height: 18px; }
  /* back */
  .card-back {
    display: flex; align-items: center; justify-content: center; gap: 16px;
  }
  .card-back .brand-dot {
    width: 44px; height: 44px; background: var(--foil);
  }
  .card-back .brand-name { color: var(--foil); font-size: 30px; }
</style>
</head>
<body>
<main class="stage">
  <section class="card card-front" aria-label="Card front">
    <div class="brand-zone">
      <span class="brand-dot"></span>
      <span class="brand-name">Harlow<br>Commercial<br>Builders</span>
    </div>
    <div class="contact-zone">
      <p class="person-name">DANIEL REYES</p>
      <p class="person-role">Managing Director</p>
      <ul class="contact-list">
        <li><svg viewBox="0 0 12 12"><path d="M2 1h3l1 3-1.5 1a7 7 0 0 0 2.5 2.5L8 6l3 1v3a1 1 0 0 1-1 1A9 9 0 0 1 1 2a1 1 0 0 1 1-1z"/></svg>044-987 654 321</li>
        <li><svg viewBox="0 0 12 12"><path d="M0 2h12v8H0z M1 3v.4l5 3.2 5-3.2V3z" fill-rule="evenodd"/></svg>hello@sitename.com</li>
        <li><svg viewBox="0 0 12 12"><circle cx="6" cy="6" r="5.5"/><path d="M6 1v10M1 6h10" stroke="#141414" stroke-width="0.8"/></svg>www.yoursitename.com</li>
      </ul>
      <p class="address">88, Street line placed here<br>30210,Region Name</p>
    </div>
  </section>
  <section class="card card-back" aria-label="Card back">
    <span class="brand-dot"></span>
    <span class="brand-name">Harlow<br>Commercial<br>Builders</span>
  </section>
</main>
</body>
</html>
```